Landscape design build company door flyer

I would like this flyer to convey a high-level of professionalism for a company that is excellent with communication with their clients as well as a company that does incredible installations

Went on vacation/holiday

```html
<!DOCTYPE html>
<html lang="en">
<head>
<meta charset="utf-8">
<title>Serene Stone Builders – Door Flyer</title>
<link href="https://fonts.googleapis.com/css2?family=Lilita+One&family=Montserrat:wght@400;500;600;700&display=swap" rel="stylesheet">
<style>
  :root{
    --navy:#0e3042;
    --yellow:#f7d117;
    --orange:#f6a21e;
    --white:#ffffff;
    --gray-text:#555b60;
    --backdrop:#9a9ea6;
  }
  html,body{margin:0;padding:0;width:1200px;height:1200px;overflow:hidden;background:var(--backdrop);}
  .flyer{position:absolute;left:20px;top:186px;width:1160px;height:827px;display:block;}
  .headline{font-family:'Lilita One',sans-serif;fill:var(--yellow);font-size:74px;}
  .subhead{font-family:'Montserrat',sans-serif;fill:var(--white);font-size:27px;font-weight:500;}
  .brand-name{font-family:'Montserrat',sans-serif;fill:var(--navy);font-size:24px;font-weight:700;}
  .brand-tagline{font-family:'Montserrat',sans-serif;fill:var(--navy);font-size:14px;font-weight:600;}
  .section-title{font-family:'Montserrat',sans-serif;fill:var(--navy);font-size:44px;font-weight:700;}
  .card-label{font-family:'Montserrat',sans-serif;fill:var(--navy);font-size:17px;font-weight:700;}
  .feature-title{font-family:'Montserrat',sans-serif;fill:var(--navy);font-size:23px;font-weight:700;}
  .feature-body{font-family:'Montserrat',sans-serif;fill:var(--gray-text);font-size:13px;}
  .area-title{font-family:'Montserrat',sans-serif;fill:var(--navy);font-size:24px;font-weight:700;}
  .area-body{font-family:'Montserrat',sans-serif;fill:var(--gray-text);font-size:16px;}
  .cta{font-family:'Montserrat',sans-serif;fill:var(--white);font-size:32px;font-weight:700;}
  .contact{font-family:'Montserrat',sans-serif;fill:var(--white);font-size:13px;}
</style>
</head>
<body>
<svg class="flyer" viewBox="0 0 1546 1102" xmlns="http://www.w3.org/2000/svg">
  <defs>
    <linearGradient id="heroTone" x1="0" y1="0" x2="1" y2="1">
      <stop offset="0" stop-color="#2a4a2c"/>
      <stop offset="0.35" stop-color="#3fb7c0"/>
      <stop offset="0.7" stop-color="#b9bcbf"/>
      <stop offset="1" stop-color="#8d9297"/>
    </linearGradient>
    <linearGradient id="pathTone" x1="0" y1="0" x2="0" y2="1">
      <stop offset="0" stop-color="#6b4a32"/>
      <stop offset="0.5" stop-color="#8a7a6a"/>
      <stop offset="1" stop-color="#3a3430"/>
    </linearGradient>
    <linearGradient id="labelTone" x1="0" y1="0" x2="1" y2="0">
      <stop offset="0" stop-color="var(--orange)"/>
      <stop offset="1" stop-color="var(--yellow)"/>
    </linearGradient>
    <clipPath id="ringClip"><circle cx="732" cy="540" r="148"/></clipPath>
  </defs>

  <rect class="flyer-bg" width="1546" height="1102" fill="var(--white)"/>

  <!-- hero -->
  <path role="img" aria-label="Photo of a lit backyard pool with stone paver deck and water features" d="M0,0 H1546 V700 L600,470 C470,330 200,320 0,470 Z" fill="url(#heroTone)"/>

  <!-- brand corner -->
  <circle cx="272" cy="-12" r="318" fill="var(--navy)"/>
  <circle cx="282" cy="-22" r="318" fill="var(--white)"/>
  <circle cx="282" cy="140" r="22" fill="var(--navy)"/>
  <text class="brand-name" x="282" y="216" text-anchor="middle">SERENE STONE BUILDERS</text>
  <text class="brand-tagline" x="282" y="237" text-anchor="middle">OUTDOOR LIVING SPACES</text>

  <!-- services heading -->
  <path d="M0,452 C160,318 440,308 606,462" fill="none" stroke="var(--navy)" stroke-width="14"/>
  <path d="M0,478 C130,395 200,360 290,358 C380,358 450,400 600,480 C460,438 380,467 290,468 C205,468 150,440 0,480 Z" fill="url(#labelTone)"/>
  <text class="section-title" x="287" y="425" text-anchor="middle">Our Services</text>

  <!-- service cards -->
  <g class="service-card">
    <rect x="65" y="500" width="232" height="167" rx="12" fill="url(#labelTone)" stroke="var(--navy)" stroke-width="2"/>
    <path role="img" aria-label="Photo of a paver patio with fire pit and lounge seating" d="M77,500 H285 A12,12 0 0 1 297,512 V625 H65 V512 A12,12 0 0 1 77,500 Z" fill="#6e7a62"/>
    <text class="card-label" x="181" y="652" text-anchor="middle">PAVER PATIOS</text>
  </g>
  <g class="service-card">
    <rect x="317" y="500" width="232" height="167" rx="12" fill="url(#labelTone)" stroke="var(--navy)" stroke-width="2"/>
    <path role="img" aria-label="Photo of a paver driveway leading to wooden garage doors" d="M329,500 H537 A12,12 0 0 1 549,512 V625 H317 V512 A12,12 0 0 1 329,500 Z" fill="#9a8670"/>
    <text class="card-label" x="433" y="652" text-anchor="middle">PAVER DRIVEWAYS</text>
  </g>
  <g class="service-card">
    <rect x="65" y="690" width="232" height="170" rx="12" fill="url(#labelTone)" stroke="var(--navy)" stroke-width="2"/>
    <path role="img" aria-label="Photo of stone block retaining walls with steps" d="M77,690 H285 A12,12 0 0 1 297,702 V815 H65 V702 A12,12 0 0 1 77,690 Z" fill="#6d6c68"/>
    <text class="card-label" x="177" y="845" text-anchor="middle">RETAINING WALLS</text>
  </g>
  <g class="service-card">
    <rect x="317" y="690" width="232" height="170" rx="12" fill="url(#labelTone)" stroke="var(--navy)" stroke-width="2"/>
    <path role="img" aria-label="Photo of a wooden deck with pergola and chairs" d="M329,690 H537 A12,12 0 0 1 549,702 V815 H317 V702 A12,12 0 0 1 329,690 Z" fill="#8a5238"/>
    <text class="card-label" x="436" y="844" text-anchor="middle">DECKS &amp; RAILINGS</text>
  </g>
  <g class="service-card">
    <rect x="65" y="883" width="232" height="169" rx="12" fill="url(#labelTone)" stroke="var(--navy)" stroke-width="2"/>
    <path role="img" aria-label="Photo of a modern backyard pool beside a house" d="M77,883 H285 A12,12 0 0 1 297,895 V1007 H65 V895 A12,12 0 0 1 77,883 Z" fill="#5fb0b0"/>
    <text class="card-label" x="177" y="1036" text-anchor="middle">POOLS</text>
  </g>
  <g class="service-card">
    <rect x="317" y="883" width="232" height="169" rx="12" fill="url(#labelTone)" stroke="var(--navy)" stroke-width="2"/>
    <path role="img" aria-label="Photo of an outdoor stone fireplace in a garden" d="M329,883 H537 A12,12 0 0 1 549,895 V1007 H317 V895 A12,12 0 0 1 329,883 Z" fill="#7a7260"/>
    <text class="card-label" x="433" y="1038" text-anchor="middle">FIREPITS &amp; FIREPLACES</text>
  </g>

  <!-- headline panel -->
  <path d="M820,430 C950,350 1150,300 1546,430 V630 C1400,700 1250,740 1100,720 C1000,705 900,670 820,640 Z" fill="var(--navy)"/>
  <path d="M1080,722 C1300,748 1450,700 1546,645 V690 C1440,742 1280,752 1080,722 Z" fill="url(#labelTone)"/>
  <path d="M840,640 C900,670 960,690 1000,700" fill="none" stroke="var(--yellow)" stroke-width="3"/>

  <circle cx="732" cy="540" r="154" fill="var(--navy)"/>
  <rect role="img" aria-label="Photo of lit stepping stones set in dark pebbles" x="584" y="392" width="296" height="296" clip-path="url(#ringClip)" fill="url(#pathTone)"/>
  <circle cx="732" cy="540" r="150" fill="none" stroke="var(--yellow)" stroke-width="4"/>

  <text class="headline" x="1465" y="455" text-anchor="end">It’s Time to</text>
  <text class="headline" x="1465" y="532" text-anchor="end">Discover Your Zen</text>
  <text class="subhead" x="1465" y="593" text-anchor="end">From vision to reality, let us bring your</text>
  <text class="subhead" x="1465" y="627" text-anchor="end">dream outdoor space to life.</text>

  <!-- features -->
  <g class="feature">
    <circle cx="618" cy="730" r="17" fill="url(#labelTone)"/>
    <text class="feature-title" x="643" y="740">Distinctive Design</text>
    <text class="feature-body" x="643" y="763">Stunning designs that consider your unique vision while</text>
    <text class="feature-body" x="643" y="780">seamlessly blending beauty and function.</text>
  </g>
  <g class="feature">
    <circle cx="618" cy="812" r="17" fill="url(#labelTone)"/>
    <text class="feature-title" x="643" y="822">Uncompromising Craftsmanship</text>
    <text class="feature-body" x="643" y="843">We consider our work 50% art, and 50% construction. We’re</text>
    <text class="feature-body" x="643" y="860">obsessive... and proud of it!</text>
  </g>
  <g class="feature">
    <circle cx="618" cy="894" r="17" fill="url(#labelTone)"/>
    <text class="feature-title" x="643" y="903">Exceptional Service</text>
    <text class="feature-body" x="643" y="926">From initial estimate, final walkthrough, and beyond, we’re</text>
    <text class="feature-body" x="643" y="943">driven to satisfy our clients.</text>
  </g>

  <line x1="1069" y1="755" x2="1069" y2="952" stroke="#9aa0a4" stroke-width="2"/>

  <g class="service-area">
    <text class="area-title" x="1090" y="793">Proudly Serving Clients in</text>
    <text class="area-title" x="1090" y="827">and around Seattle Since 2018</text>
    <text class="area-body" x="1090" y="868">Headquartered in Sammamish, we typically</text>
    <text class="area-body" x="1090" y="889">consider projects in Eastside Seattle, including the</text>
    <text class="area-body" x="1090" y="910">areas of Bellevue, Issaquah, Kirkland, Redmond,</text>
    <text class="area-body" x="1090" y="931">and Sammamish</text>
  </g>

  <!-- footer -->
  <path d="M515,1102 C580,1010 680,975 780,970 C680,985 600,1030 560,1102 Z" fill="url(#labelTone)"/>
  <path d="M550,1102 C610,1010 700,975 800,972 C1100,965 1300,1010 1546,945 V1102 Z" fill="var(--navy)"/>

  <text class="cta" x="660" y="1052">Call Us Now!</text>
  <g class="phone-icon">
    <circle cx="897" cy="1041" r="15" fill="var(--orange)"/>
    <path d="M890,1033 c1,-2 3,-2 4,0 l2,3 c1,1 0,3 -1,3 c1,3 3,5 6,6 c0,-1 2,-2 3,-1 l3,2 c2,1 2,3 0,4 c-2,2 -5,2 -8,0 c-4,-3 -8,-7 -10,-11 c-1,-2 -1,-4 1,-6 z" fill="var(--navy)"/>
  </g>
  <text class="cta" x="920" y="1052">(253) 555-0147</text>

  <g class="pin-icon">
    <path d="M1201,1027 a6,6 0 0 1 6,6 c0,4 -6,10 -6,10 c0,0 -6,-6 -6,-10 a6,6 0 0 1 6,-6 z" fill="var(--yellow)"/>
    <circle cx="1201" cy="1033" r="2.2" fill="var(--navy)"/>
  </g>
  <text class="contact" x="1216" y="1038">1820 Cedar Grove Lane Sammamish, WA 98074</text>
  <g class="web-icon" fill="none" stroke="var(--yellow)" stroke-width="1.2">
    <circle cx="1201" cy="1055" r="5.5"/>
    <ellipse cx="1201" cy="1055" rx="2.5" ry="5.5"/>
    <line x1="1195.5" y1="1055" x2="1206.5" y2="1055"/>
  </g>
  <text class="contact" x="1216" y="1060">www.serenestonebuilders.com</text>
</svg>
</body>
</html>
```